24 Super Fantastic Banners 4 campaigns

I need 4 campaigns to have banners made, 6 banner sizes each so 24 total banners. Here are the landing pages with the messaging.

http://www.examplebizdirectory.test/Sandy-UT/Pellworth-Medical-48271.html

http://www.examplebizdirectory.test/Darvell-Law-Group-48272.html

http://www.examplebizdirectory.test/Vuloran-48273.html

http://www.examplebizdirectory.test/Starqueb-com-48274.html

Need to get done asap. Much more work can be following right after. Here are the sizes

Sorry fix a typo. These sizes:

300 X 50
300x250
320 X50
216 X36
168 X 28
120 X 20

Medical

Requirements
Must have
• Must have phone number in the display for call to action

```html
<!DOCTYPE html>
<html lang="en">
<head>
<meta charset="utf-8">
<title>Darvell Law Group – Banner Set</title>
<link rel="stylesheet" href="https://fonts.googleapis.com/css2?family=Roboto+Condensed:wght@700&family=Open+Sans:wght@400&family=PT+Serif:wght@700&display=swap">
<style>
  :root {
    --canvas-top: #8e8c8b;
    --canvas-bottom: #a09e9d;
    --brand-red: #b3103f;
    --band-grey: #5b5b5b;
    --panel-white: #ffffff;
    --panel-shade: #d9d9d9;
    --logo-grey: #6a6a6a;
    --text-white: #ffffff;
    --photo-light: #d9c4b8;
    --photo-dark: #6f5a55;
  }
  * { box-sizing: border-box; margin: 0; padding: 0; }
  html, body { width: 969px; height: 1200px; overflow: hidden; }
  body {
    position: relative;
    background: linear-gradient(180deg, var(--canvas-top), var(--canvas-bottom));
    font-family: "Open Sans", sans-serif;
  }

  /* ---------- strip banner (300 x 50 design units, 1 unit = 1em of the strip) ---------- */
  .strip {
    position: absolute;
    width: 300em;
    height: 50em;
    background: var(--band-grey);
    overflow: hidden;
  }
  .strip--wide { width: 320em; }
  .strip__red {
    position: absolute; left: 0; top: 0; right: 0; height: 37em;
    background: var(--brand-red);
  }
  .strip__logo-shade {
    position: absolute; left: 0; top: 0; width: 98em; height: 50em;
    background: var(--panel-shade);
    clip-path: polygon(0 0, 88% 0, 100% 50%, 92% 100%, 0 100%);
  }
  .strip__logo {
    position: absolute; left: 0; top: 0; width: 92em; height: 50em;
    background: var(--panel-white);
    clip-path: polygon(0 0, 90% 0, 100% 50%, 90% 100%, 0 100%);
    display: flex; align-items: center; padding-left: 4em;
  }
  .logo-name {
    display: block;
    font-family: "Open Sans", sans-serif; font-weight: 400;
    color: var(--logo-grey); white-space: nowrap; letter-spacing: -0.02em;
  }
  .strip .logo-name { font-size: 9em; }

  .strip__headline { position: absolute; left: 97em; top: 5em; }
  .strip__headline span {
    display: block;
    font-family: "Roboto Condensed", sans-serif; font-weight: 700;
    color: var(--text-white); font-size: 10.5em; line-height: 1.2;
    white-space: nowrap; letter-spacing: -0.01em;
  }
  .strip__sub { position: absolute; left: 117em; top: 20em; }
  .strip__sub span {
    display: block;
    color: var(--text-white); font-size: 9em; line-height: 1.2; white-space: nowrap;
  }
  .strip--wide .strip__headline { left: 99em; }
  .strip--wide .strip__sub { left: 120em; }

  .strip__photo {
    position: absolute; right: 2em; top: 2em; width: 40em; height: 30em;
    background: linear-gradient(90deg, var(--photo-light), var(--photo-dark));
  }
  .strip--wide .strip__photo { right: 18em; }

  .phone-box {
    position: absolute;
    background: var(--panel-white);
    box-shadow: 0 0.05em 0.2em rgba(0,0,0,.35);
    display: flex; align-items: center; justify-content: center;
    font-family: "PT Serif", serif; font-weight: 700; color: var(--brand-red);
    white-space: nowrap;
  }
  .phone-box span { display: block; }
  .strip .phone-box { right: 4em; top: 29em; width: 84em; height: 19em; border-radius: 2.5em; }
  .strip--wide .phone-box { right: 8em; }
  .strip .phone-box span { font-size: 10em; }

  .size-120 { left: 393px; top: 77px;  font-size: 0.853px; }
  .size-168 { left: 341px; top: 139px; font-size: 1.195px; }
  .size-216 { left: 290px; top: 226px; font-size: 1.536px; }
  .size-300 { left: 201px; top: 341px; font-size: 2.133px; }
  .size-320 { left: 179px; top: 469px; font-size: 2.133px; }

  /* ---------- box banner 300 x 250 ---------- */
  .box {
    position: absolute; left: 201px; top: 623px;
    width: 300em; height: 250em; font-size: 2.133px;
    background: var(--brand-red); overflow: hidden;
  }
  .box__arc { position: absolute; left: 0; top: 0; width: 300em; height: 76em; }
  .box__logo {
    position: absolute; left: 0; top: 14em; width: 300em;
    display: flex; justify-content: center;
  }
  .box__logo .logo-name { font-size: 29em; }
  .box__photo {
    position: absolute; left: 162em; top: 50em; width: 138em; height: 165em;
    background: linear-gradient(100deg, var(--photo-light) 0%, var(--photo-dark) 100%);
  }
  .box__band {
    position: absolute; left: 0; top: 215em; width: 300em; height: 35em;
    background: var(--band-grey); border-top: 3em solid var(--panel-white);
  }
  .box__copy { position: absolute; left: 6em; top: 94em; color: var(--text-white); }
  .box__line1, .box__line2 {
    font-family: "Roboto Condensed", sans-serif; font-weight: 700; line-height: 1.1; white-space: nowrap;
  }
  .box__line1 { font-size: 30em; }
  .box__line2 { font-size: 22em; }
  .box__line3 { font-size: 16em; line-height: 1.4; white-space: nowrap; }
  .box .phone-box { left: 61em; top: 195em; width: 178em; height: 40em; border-radius: 6em; }
  .box .phone-box span { font-size: 22em; }
</style>
</head>
<body>

  <div class="strip size-120">
    <div class="strip__red"></div>
    <div class="strip__logo-shade"></div>
    <div class="strip__logo"><span class="logo-name">Darvell law group</span></div>
    <div class="strip__headline"><span>Your Victory and Protection</span></div>
    <div class="strip__sub"><span>is our commitment</span></div>
    <div class="strip__photo" role="img" aria-label="Photo of two smiling lawyers giving a thumbs up"></div>
    <div class="phone-box"><span>(888) 555-0147</span></div>
  </div>

  <div class="strip size-168">
    <div class="strip__red"></div>
    <div class="strip__logo-shade"></div>
    <div class="strip__logo"><span class="logo-name">Darvell law group</span></div>
    <div class="strip__headline"><span>Your Victory and Protection</span></div>
    <div class="strip__sub"><span>is our commitment</span></div>
    <div class="strip__photo" role="img" aria-label="Photo of two smiling lawyers giving a thumbs up"></div>
    <div class="phone-box"><span>(888) 555-0147</span></div>
  </div>

  <div class="strip size-216">
    <div class="strip__red"></div>
    <div class="strip__logo-shade"></div>
    <div class="strip__logo"><span class="logo-name">Darvell law group</span></div>
    <div class="strip__headline"><span>Your Victory and Protection</span></div>
    <div class="strip__sub"><span>is our commitment</span></div>
    <div class="strip__photo" role="img" aria-label="Photo of two smiling lawyers giving a thumbs up"></div>
    <div class="phone-box"><span>(888) 555-0147</span></div>
  </div>

  <div class="strip size-300">
    <div class="strip__red"></div>
    <div class="strip__logo-shade"></div>
    <div class="strip__logo"><span class="logo-name">Darvell law group</span></div>
    <div class="strip__headline"><span>Your Victory and Protection</span></div>
    <div class="strip__sub"><span>is our commitment</span></div>
    <div class="strip__photo" role="img" aria-label="Photo of two smiling lawyers giving a thumbs up"></div>
    <div class="phone-box"><span>(888) 555-0147</span></div>
  </div>

  <div class="strip strip--wide size-320">
    <div class="strip__red"></div>
    <div class="strip__logo-shade"></div>
    <div class="strip__logo"><span class="logo-name">Darvell law group</span></div>
    <div class="strip__headline"><span>Your Victory and Protection</span></div>
    <div class="strip__sub"><span>is our commitment</span></div>
    <div class="strip__photo" role="img" aria-label="Photo of two smiling lawyers giving a thumbs up"></div>
    <div class="phone-box"><span>(888) 555-0147</span></div>
  </div>

  <div class="box">
    <div class="box__photo" role="img" aria-label="Photo of a smiling woman and man in business suits giving thumbs up"></div>
    <svg class="box__arc" viewBox="0 0 300 76" preserveAspectRatio="none" aria-hidden="true">
      <path d="M0 0 H300 V62 Q150 84 0 62 Z" fill="#d9d9d9"/>
      <path d="M0 0 H300 V58 Q150 78 0 58 Z" fill="#ffffff"/>
    </svg>
    <div class="box__logo"><span class="logo-name">Darvell law group</span></div>
    <div class="box__copy">
      <div class="box__line1">Your Victory</div>
      <div class="box__line2">and Protection</div>
      <div class="box__line3">is our commitment</div>
    </div>
    <div class="box__band"></div>
    <div class="phone-box"><span>(888) 555-0147</span></div>
  </div>

</body>
</html>
```